New Business Card Design Project VORASTI-Italy

we are VORASTI-Italy
our company in the market for 3 years we are luxury cosmetic company and its about time for a facelift :)
i will like to have elegant luxurious and unique business card
that will give the person that get it a unique, luxurious and elegant impression
I'm VERY OPEN FOR NEW IDEAS , even duo i add a few files of things that i see on line and i like them

i add my logo as well
my website is VORASTI.COM
(if you would like to see the main style that we have)

Target Market(s)

adult that have money :)

Industry/Entity Type

Business

Contact Information for Business Card

Name - Paul Vorasti
Position - CEO and CO Founder
address - 4817 E Larkdale
telephone - 555-384-1962
email - paul@vorasti.com
fax - 555-384-1962
website - VORASTI.COM

Colors
000000
959595
fbee3e
ffffff

Requirements
Must have
• big logo in GOLD color
• elegant look
• impressive
Nice to have
• not must but maybe classy pattern background
• not must but maybe emblem
• maybe clear plastic business card
Should not have
• colors
• images

```html
<!DOCTYPE html>
<html lang="en">
<head>
<meta charset="utf-8">
<title>VORASTI Italy – Business Card</title>
<link rel="stylesheet" href="https://fonts.googleapis.com/css2?family=Tinos&family=Open+Sans:wght@400&display=swap">
<style>
  :root {
    --gold: #c9a33f;
    --gold-deep: #b58f2e;
    --white: #ffffff;
    --bg-dark: #1c1c1c;
    --bg-mid: #444444;
    --bg-light: #8c8c8c;
    --serif: "Tinos", "Times New Roman", serif;
    --sans: "Open Sans", Arial, sans-serif;
  }
  html, body {
    margin: 0;
    padding: 0;
    width: 1200px;
    height: 686px;
    overflow: hidden;
    background: var(--bg-dark);
  }
  .card {
    position: relative;
    width: 1200px;
    height: 686px;
    overflow: hidden;
    background: linear-gradient(200deg, var(--bg-light) 0%, var(--bg-mid) 38%, var(--bg-dark) 78%);
  }
  .brand-mark {
    position: absolute;
    left: 177px;
    top: 95px;
    width: 216px;
    height: 216px;
  }
  .brand-name {
    position: absolute;
    left: 34px;
    width: 500px;
    top: 393px;
    margin: 0;
    font-family: var(--serif);
    font-weight: 400;
    font-size: 95px;
    line-height: 1;
    text-align: center;
    color: var(--gold);
    letter-spacing: 1px;
  }
  .brand-rule {
    position: absolute;
    left: 46px;
    top: 500px;
    width: 481px;
    height: 5px;
    background: var(--gold);
  }
  .brand-origin {
    position: absolute;
    left: 34px;
    width: 500px;
    top: 526px;
    margin: 0;
    font-family: var(--serif);
    font-size: 36px;
    line-height: 1;
    text-align: center;
    color: var(--gold);
  }
  .person {
    position: absolute;
    left: 640px;
    width: 480px;
    text-align: center;
  }
  .person-name {
    position: absolute;
    left: 0;
    right: 0;
    top: 280px;
    margin: 0;
    font-family: var(--serif);
    font-weight: 400;
    font-size: 48px;
    line-height: 1;
    color: var(--gold);
    letter-spacing: 1px;
  }
  .person-role,
  .person-address {
    position: absolute;
    left: 0;
    right: 0;
    margin: 0;
    font-family: var(--sans);
    font-size: 27px;
    line-height: 1;
    color: var(--white);
  }
  .person-role { top: 334px; }
  .person-address { top: 372px; }
  .contact {
    position: absolute;
    top: 555px;
    margin: 0;
    font-family: var(--sans);
    font-size: 23px;
    line-height: 32px;
    color: var(--white);
    white-space: nowrap;
  }
  .contact-phone { left: 601px; }
  .contact-web { left: 875px; }
</style>
</head>
<body>
  <main class="card">
    <svg class="brand-mark" viewBox="0 0 216 216" aria-hidden="true">
      <circle cx="108" cy="108" r="104" fill="none" stroke="var(--gold)" stroke-width="5"/>
    </svg>
    <h1 class="brand-name">VORASTI</h1>
    <div class="brand-rule"></div>
    <p class="brand-origin">ITALY</p>

    <section class="person" style="top:0;height:686px;">
      <h2 class="person-name">Paul Vorasti</h2>
      <p class="person-role">CEO and CO Founder</p>
      <p class="person-address">4817 E Larkdale</p>
    </section>

    <p class="contact contact-phone">Tel.&nbsp; no.: 555-384-1962<br>Fax: 555-384-1962</p>
    <p class="contact contact-web">Email: paul@vorasti.com<br>website: VORASTI.COM</p>
  </main>
</body>
</html>
```